New Web Design Project

Require a website for The Bramwell Harvest. All relevant information is in the uploaded files.

website to be responsive to work on mobile.

Required in html5, css

Coding

Coded - Design and coding required

Number of Pages Required

3 page

```html
<!DOCTYPE html>
<html lang="en">
<head>
<meta charset="utf-8">
<meta name="viewport" content="width=device-width, initial-scale=1">
<title>The Bramwell Harvest Company</title>
<link href="https://fonts.googleapis.com/css2?family=Lato:wght@400;700;900&family=Roboto+Slab:wght@700&display=swap" rel="stylesheet">
<style>
:root{
  --green:#8cc63f;
  --green-dark:#76b02e;
  --green-soft:#e9f4da;
  --orange:#f7941d;
  --orange-deep:#f08a12;
  --ink:#1d1d1d;
  --text:#555;
  --muted:#777;
  --line:#e6e6e6;
  --white:#fff;
}
*{box-sizing:border-box;margin:0;padding:0}
html,body{width:1200px;height:4089px;overflow:hidden}
body{position:relative;font-family:"Lato",sans-serif;color:var(--text);background:var(--white)}
.abs{position:absolute}
.slab{font-family:"Roboto Slab",serif;font-weight:700;color:var(--ink);letter-spacing:.5px}
.mark{display:block;width:34px;height:8px;border-radius:4px;background:var(--green)}
.btn{display:inline-flex;align-items:center;gap:10px;font-weight:700;font-size:14px;color:var(--white);text-transform:uppercase;border-radius:4px;justify-content:center}
.btn .dot{width:14px;height:14px;border-radius:50%;background:var(--white);position:relative}
.btn .dot::after{content:"";position:absolute;left:4px;top:4px;border-left:6px solid var(--orange);border-top:3px solid transparent;border-bottom:3px solid transparent}

/* top bar & header */
.topbar{left:0;top:0;width:1200px;height:43px;background:var(--green);color:var(--white);font-size:14px}
.topbar span{position:absolute;top:13px}
.header{left:0;top:43px;width:1200px;height:76px;background:var(--white);z-index:5}
.logo{left:111px;top:0;width:130px;height:108px;background:var(--white);display:flex;flex-direction:column;align-items:center;justify-content:center;gap:8px;box-shadow:0 2px 6px rgba(0,0,0,.08)}
.logo i{width:20px;height:20px;border-radius:50%;background:var(--orange)}
.logo b{font-size:16px;font-weight:900;color:var(--ink);text-align:center;line-height:1.2}
.nav{left:323px;top:30px;display:flex;gap:28px;font-size:14px;font-weight:700;color:var(--ink)}
.nav .on{color:var(--green)}
.quote{left:930px;top:13px;width:159px;height:50px;background:var(--orange)}

/* hero */
.hero{left:0;top:119px;width:1200px;height:516px;background:linear-gradient(120deg,#3a3a3a 0%,#9a8c80 35%,#d8d1ca 60%,#7c7772 100%)}
.hero h1{position:absolute;left:0;top:190px;width:1200px;text-align:center;font-size:58px;line-height:66px;color:var(--white);text-shadow:0 2px 6px rgba(0,0,0,.35);font-family:"Roboto Slab",serif}

/* about */
.about-h{left:111px;top:708px}
.about-h h2{font-size:44px;margin-top:8px}
.about-p{left:111px;top:800px;width:447px;font-size:16px;line-height:31px;text-align:justify}
.about-btn{left:111px;top:1072px;width:173px;height:52px;background:var(--orange)}
.about-img{left:651px;top:719px;width:462px;height:368px;background:var(--white);box-shadow:0 0 6px rgba(0,0,0,.2);padding:4px}
.about-img div{width:100%;height:100%;background:linear-gradient(135deg,#3b3530,#6f6559 50%,#c8bfb3)}
.badge{left:619px;top:955px;width:148px;height:153px;background:var(--green);border:5px solid var(--white);outline:3px solid var(--green);color:var(--white);text-align:center;font-family:"Roboto Slab",serif;font-weight:700;font-size:18px;line-height:27px;padding-top:22px}
.badge strong{display:block;font-size:32px;line-height:36px}

/* services */
.sec-head{left:0;width:1200px;text-align:center}
.sec-head .mark{margin:0 auto 10px}
.sec-head h2{font-size:44px}
.services-sub{left:270px;top:1328px;width:660px;text-align:center;font-size:16px;line-height:26px}
.service{top:1440px;width:310px;text-align:center}
.service .ic{width:120px;height:120px;border-radius:50%;margin:0 auto;background:var(--green-soft)}
.service h3{margin-top:26px;font-size:19px}
.service hr{width:32px;border:0;border-top:3px solid var(--orange);margin:14px auto}
.service p{font-size:14px;line-height:24px;color:var(--muted)}

/* team */
.team{left:0;top:1785px;width:1200px;height:429px;background:linear-gradient(90deg,var(--orange-deep),var(--orange) 60%,#f9a030)}
.member{top:53px;width:243px;height:325px;background:var(--white)}
.member .ph{margin:3px;height:179px;background:linear-gradient(160deg,#cfcfcf,#8d8d8d)}
.member h4{margin-top:25px;text-align:center;font-size:14px;color:var(--ink);font-weight:700}
.member p{text-align:center;font-size:14px;margin-top:10px;color:var(--muted)}
.member .soc{display:flex;justify-content:center;gap:12px;margin-top:16px}
.member .soc span{width:38px;height:38px;border-radius:50%;border:2px solid var(--green)}
.team-copy{left:680px;top:55px;width:409px;text-align:right;color:var(--white)}
.team-copy .mark{background:var(--white);margin-left:auto}
.team-copy h2{color:var(--white);font-size:42px;margin-top:10px}
.team-copy p{margin-top:16px;font-size:16px;line-height:31px;text-align:justify;text-align-last:right}
.team-btn{left:936px;top:342px;width:151px;height:51px;border:2px solid var(--white)}

/* news */
.news{width:473px;height:236px;background:var(--white);box-shadow:0 0 8px rgba(0,0,0,.14);display:flex}
.news .ph{width:216px;height:230px;margin:3px;background:linear-gradient(135deg,#3d2f26,#8a6d55 60%,#cbb9a5)}
.news .body{padding:28px 0 0 30px;width:240px}
.news h4{font-size:14px;font-weight:700;color:var(--ink)}
.news .date{margin-top:14px;font-size:13px;color:var(--muted);display:flex;align-items:center;gap:10px}
.news .date i{width:12px;height:12px;background:var(--orange);border-radius:2px}
.news p{margin-top:16px;font-size:14px;line-height:26px}
.news a{display:block;margin-top:10px;font-size:12px;font-weight:700;color:var(--orange);text-decoration:underline}

/* testimonials */
.testi-bg{left:0;top:2980px;width:1200px;height:504px;background:linear-gradient(180deg,#fff 0%,#f1f1f1 40%,#e8e8e8 100%)}
.testi{top:3150px;width:480px;height:222px;background:var(--white);box-shadow:0 0 8px rgba(0,0,0,.1);text-align:center;padding-top:26px}
.testi .who{display:flex;align-items:center;justify-content:center;gap:18px;font-size:14px;color:var(--ink)}
.testi .who i{width:58px;height:58px;border-radius:50%;background:linear-gradient(135deg,#9aa3ab,#5d666e)}
.testi p{margin:26px 38px 0;font-size:13px;line-height:31px;color:var(--muted)}

/* contact */
.contact{left:0;top:3484px;width:1200px;height:516px;background:linear-gradient(180deg,rgba(140,198,63,.95),rgba(118,176,46,.95))}
.contact .mark{background:var(--white)}
.contact h2{color:var(--white)}
.field{height:53px;border:1px solid rgba(255,255,255,.7);color:var(--white);font-size:15px;padding:17px 18px}
.send{left:513px;top:406px;width:174px;height:51px;background:var(--orange)}

.footer{left:0;top:4000px;width:1200px;height:89px;background:var(--white);text-align:center;font-size:14px;padding-top:39px}
</style>
</head>
<body>

<div class="abs topbar">
  <span style="left:730px">✉&nbsp; hello@bramwellharvest.example</span>
  <span style="left:966px;font-weight:700">☎&nbsp; 1 555 010 2030</span>
</div>

<section class="abs hero" role="img" aria-label="Photo of a smiling business team meeting around a laptop">
  <h1>THE BRAMWELL HARVEST<br>COMPANY</h1>
</section>

<header class="abs header">
  <div class="abs logo"><i></i><b>The Bramwell<br>Harvest</b></div>
  <nav class="abs nav"><span class="on">HOME</span><span>ABOUT US</span><span>OUR SERVICES</span><span>LATEST BLOG</span><span>CONTACT US</span></nav>
  <a class="abs btn quote">Get a quote <span class="dot"></span></a>
</header>

<section>
  <div class="abs about-h"><span class="mark"></span><h2 class="slab">ABOUT US</h2></div>
  <p class="abs about-p">The Bramwell Harvest Company was incorporated with the objective of introducing new vendors to the Canadian market through a trusted and mutual business relation. It was set up by Darius Kelleher and Milo Andreou who have a combined experience of over 45 years in the fresh produce business. With Darius's expertise in global sourcing and Milo's vast connection and know how of the Canadian market, we have helped our existing partners</p>
  <a class="abs btn about-btn">More about us <span class="dot"></span></a>
  <div class="abs about-img"><div role="img" aria-label="Photo of business partners shaking hands over a restaurant lunch"></div></div>
  <div class="abs badge"><strong>45</strong>YEARS OF<br>EXPERIENCE</div>
</section>

<section>
  <div class="abs sec-head" style="top:1226px"><span class="mark"></span><h2 class="slab">OUR SERVICES</h2></div>
  <p class="abs services-sub">Sed ut perspiciatis unde omnis iste natus error sit voluptatem accusantium doloremque laudantium, totam rem aperiam, eaque ipsa quae ab illo inventor</p>
  <div class="abs service" style="left:108px"><div class="ic" role="img" aria-label="Service icon: sourcing"></div><h3 class="slab">LOREM IPSUM</h3><hr><p>Sed ut perspiciatis unde omnis iste<br>natus error sit voluptatem accusadoloremque<br>laudantium, totam rem aperiam.</p></div>
  <div class="abs service" style="left:445px"><div class="ic" role="img" aria-label="Service icon: partnership"></div><h3 class="slab">LOREM IPSUM</h3><hr><p>Sed ut perspiciatis unde omnis iste<br>natus error sit voluptatem accusadoloremque<br>laudantium, totam rem aperiam.</p></div>
  <div class="abs service" style="left:781px"><div class="ic" role="img" aria-label="Service icon: trade finance"></div><h3 class="slab">LOREM IPSUM</h3><hr><p>Sed ut perspiciatis unde omnis iste<br>natus error sit voluptatem accusadoloremque<br>laudantium, totam rem aperiam.</p></div>
</section>

<section class="abs team">
  <div class="abs member" style="left:102px">
    <div class="ph" role="img" aria-label="Portrait of the founder and president"></div>
    <h4>DARIUS KELLEHER</h4><p>Founder &amp; President</p>
    <div class="soc"><span></span><span></span><span></span></div>
  </div>
  <div class="abs member" style="left:368px">
    <div class="ph" role="img" aria-label="Portrait of the co-founder"></div>
    <h4>MILO ANDREOU</h4><p>Founder</p>
    <div class="soc"><span></span><span></span><span></span></div>
  </div>
  <div class="abs team-copy">
    <span class="mark"></span>
    <h2 class="slab">MEET OUR TEAM</h2>
    <p>Sed ut perspiciatis unde omnis iste natus error sit voluptatem accusantium doloremque laudantium, totam rem aperiam, eaque ipsa quae ab illo inventore veritatis et quasi architecto beatae vitae dicta sunt explicabo. Nemo enim ipsam voluptatem quia voluptas sit aspernatur aut odit aut fugit</p>
  </div>
  <a class="abs btn team-btn">Read more <span class="dot"></span></a>
</section>

<section>
  <div class="abs sec-head" style="top:2296px"><span class="mark"></span><h2 class="slab">LATEST EXPORTING NEWS</h2></div>
  <article class="abs news" style="left:111px;top:2430px"><div class="ph" role="img" aria-label="Photo of friends toasting at a dinner table"></div><div class="body"><h4>LOREM IPSUM DOLOR SIT</h4><div class="date"><i></i>Nov 04 , 2020</div><p>Sed ut perspiciatis unde omnis iste natus error sit voluptatem accusantium doloremque</p><a>LEARN MORE »</a></div></article>
  <article class="abs news" style="left:616px;top:2430px"><div class="ph" role="img" aria-label="Photo of a waiter greeting a restaurant guest"></div><div class="body"><h4>LOREM IPSUM DOLOR SIT</h4><div class="date"><i></i>Nov 04 , 2020</div><p>Sed ut perspiciatis unde omnis iste natus error sit voluptatem accusantium doloremque</p><a>LEARN MORE »</a></div></article>
  <article class="abs news" style="left:111px;top:2704px"><div class="ph" role="img" aria-label="Photo of chefs preparing food in a kitchen" style="background:linear-gradient(135deg,#e9e6e2,#b7ada3 60%,#6b5a4b)"></div><div class="body"><h4>LOREM IPSUM DOLOR SIT</h4><div class="date"><i></i>Nov 04 , 2020</div><p>Sed ut perspiciatis unde omnis iste natus error sit voluptatem accusantium doloremque</p><a>LEARN MORE »</a></div></article>
  <article class="abs news" style="left:616px;top:2704px"><div class="ph" role="img" aria-label="Photo of a sommelier pouring wine"></div><div class="body"><h4>LOREM IPSUM DOLOR SIT</h4><div class="date"><i></i>Nov 04 , 2020</div><p>Sed ut perspiciatis unde omnis iste natus error sit voluptatem accusantium doloremque</p><a>LEARN MORE »</a></div></article>
</section>

<section>
  <div class="abs testi-bg"></div>
  <div class="abs sec-head" style="top:3031px"><span class="mark"></span><h2 class="slab">TESTIMONIALS</h2></div>
  <div class="abs testi" style="left:111px"><div class="who"><i role="img" aria-label="Client portrait"></i><span><b>OWEN MARSH ,</b> Businessman</span></div><p>At vero eos et accusamus et iusto odio dignissimos ducimus qui blanditiis praesentium voluptatum deleniti atque corrupti quos dolores et quas molestias excepturi sint occaecati.</p></div>
  <div class="abs testi" style="left:608px"><div class="who"><i role="img" aria-label="Client portrait"></i><span><b>OWEN MARSH ,</b> Businessman</span></div><p>At vero eos et accusamus et iusto odio dignissimos ducimus qui blanditiis praesentium voluptatum deleniti atque corrupti quos dolores et quas molestias excepturi sint occaecati.</p></div>
</section>

<section class="abs contact">
  <div class="abs sec-head" style="top:54px"><span class="mark"></span><h2 class="slab">CONTACT US</h2></div>
  <div class="abs field" style="left:273px;top:150px;width:319px">First Name *</div>
  <div class="abs field" style="left:606px;top:150px;width:321px">Last Name *</div>
  <div class="abs field" style="left:273px;top:218px;width:319px">Email Address *</div>
  <div class="abs field" style="left:606px;top:218px;width:321px">Phone No *</div>
  <div class="abs field" style="left:273px;top:286px;width:654px;height:96px">Message *</div>
  <a class="abs btn send">Submit now <span class="dot"></span></a>
</section>

<footer class="abs footer">© 2020 The Bramwell Harvest. All Rights Reserved</footer>

</body>
</html>
```